Lumo Brew Premium Matcha brand Label

This is a label design project for a luxury tea brand. Feel free to be creative within the guidelines.
Attached to this project is a document called “Private Label Design Requirements” with the design guidelines and template. There is another document called "Lumo Brew Packaging Instructions" this has more details necessary to stick to the guidelines in the first document.

I have also attached the certifications to be included as well as different variations of the logo for you to use.

If you have any questions, I am here.
Updates

Target Market(s)

Young, active, fun, enjoy the finer things

```html
<!DOCTYPE html>
<html lang="en">
<head>
<meta charset="utf-8">
<title>Lumo Brew Premium Organic Ceremonial Matcha Label</title>
<link rel="stylesheet" href="https://fonts.googleapis.com/css2?family=Jost:ital,wght@0,400;0,500;1,400&family=Oswald:wght@400&display=swap">
<style>
  :root {
    --page-bg: #e9f6de;
    --matcha-green: #62ff1c;
    --pattern-tone: #f1f3ef;
    --ink: #1b1b1b;
    --white: #ffffff;
    --heading-green: #4fd616;
  }
  * { box-sizing: border-box; margin: 0; padding: 0; }
  html, body { width: 1200px; height: 800px; overflow: hidden; }
  body {
    background: var(--page-bg);
    font-family: "Jost", sans-serif;
    color: var(--ink);
    position: relative;
  }
  .label {
    position: absolute;
    left: 40px; top: 306px;
    width: 1120px; height: 188px;
  }
  .label__pattern-band {
    position: absolute; left: 0; top: 0; width: 100%; height: 74px;
    background: linear-gradient(180deg, #f6f7f4 0%, var(--pattern-tone) 100%);
  }
  .label__color-band {
    position: absolute; left: 0; top: 74px; width: 100%; height: 114px;
    background: var(--matcha-green);
  }
  .storage-note {
    position: absolute; left: 57px; top: 22px;
    width: 217px; height: 30px;
    border: 1.5px solid var(--ink); border-radius: 5px;
    background: var(--white);
    font-weight: 500; font-size: 12.5px; letter-spacing: 0.4px;
    display: flex; align-items: center; justify-content: center;
    text-transform: uppercase;
  }
  .distributor {
    position: absolute; left: 59px; top: 80px;
    font-size: 13px; line-height: 17px; color: var(--ink);
  }
  .distributor__title { font-style: italic; }
  .origin {
    position: absolute; left: 59px; top: 142px;
    font-size: 11px; letter-spacing: 0.8px; color: var(--white);
    text-transform: uppercase;
  }
  .cert-badges {
    position: absolute; left: 206px; top: 138px;
    display: flex; gap: 20px;
  }
  .cert-badge { width: 30px; height: 30px; background: var(--white); border: 1.5px solid #9aa59a; }
  .cert-badge--round { border-radius: 50%; }
  .brand-mark {
    position: absolute; left: 525px; top: 3px;
    width: 70px; height: 70px; border-radius: 50%;
    background: var(--matcha-green);
    display: flex; align-items: center; justify-content: center;
  }
  .brand-mark__name {
    font-size: 11px; font-weight: 500; color: var(--white);
  }
  .product-title {
    position: absolute; left: 300px; width: 520px; text-align: center;
    font-family: "Oswald", sans-serif; font-weight: 400; color: var(--ink);
  }
  .product-title--line1 { top: 88px; font-size: 20px; letter-spacing: 2px; }
  .product-title--line2 { top: 108px; font-size: 34px; letter-spacing: 1.5px; line-height: 1.2; }
  .net-weight {
    position: absolute; left: 300px; width: 520px; top: 147px; text-align: center;
    font-size: 14px; color: var(--white); letter-spacing: 0.3px;
  }
  .panel-info { position: absolute; left: 847px; }
  .panel-info__heading { font-style: italic; font-size: 14px; }
  .ingredients { top: 20px; font-size: 12.5px; line-height: 14px; }
  .ingredients .panel-info__heading { color: var(--heading-green); margin-bottom: 5px; }
  .instructions { top: 84px; }
  .instructions .panel-info__heading { color: var(--ink); margin-bottom: 3px; }
  .instructions__list { list-style: none; font-size: 12.5px; line-height: 15px; color: var(--white); }
  .instructions__list li { display: flex; align-items: center; gap: 8px; }
  .instructions__list svg { flex: none; }
</style>
</head>
<body>
  <section class="label" aria-label="Lumo Brew matcha tin label">
    <div class="label__pattern-band" role="img" aria-label="Soft pale leaf pattern band"></div>
    <div class="label__color-band"></div>

    <div class="storage-note">Keep refrigerated for quality</div>

    <div class="distributor">
      <p class="distributor__title">Distributed by</p>
      <p>Lumo Brew Co. | Maple Falls, Ga</p>
      <p>Certified Organic by Verdan</p>
    </div>
    <p class="origin">Product of Japan</p>
    <div class="cert-badges">
      <span class="cert-badge"></span>
      <span class="cert-badge cert-badge--round"></span>
    </div>

    <div class="brand-mark"><span class="brand-mark__name">Lumo Brew</span></div>

    <h1 class="product-title product-title--line1">PREMIUM ORGANIC</h1>
    <h2 class="product-title product-title--line2">CEREMONIAL MATCHA</h2>
    <p class="net-weight">Net Wt: 30g (1.06oz)</p>

    <div class="panel-info ingredients">
      <p class="panel-info__heading">Ingredients:</p>
      <p>Premium Organic Japanese</p>
      <p>Matcha Green Tea</p>
    </div>

    <div class="panel-info instructions">
      <p class="panel-info__heading">Instructions:</p>
      <ul class="instructions__list">
        <li><svg width="8" height="8" viewBox="0 0 8 8"><circle cx="4" cy="4" r="3.5" fill="#1b1b1b"/></svg>2 tsp of Matcha</li>
        <li><svg width="8" height="8" viewBox="0 0 8 8"><circle cx="4" cy="4" r="3.5" fill="#1b1b1b"/></svg>2oz of Water (170-180 degrees F)</li>
        <li><svg width="8" height="8" viewBox="0 0 8 8"><circle cx="4" cy="4" r="3.5" fill="#1b1b1b"/></svg>Whisk in a W formation until frothy</li>
        <li><svg width="8" height="8" viewBox="0 0 8 8"><circle cx="4" cy="4" r="3.5" fill="#1b1b1b"/></svg>Sweeten to taste</li>
      </ul>
    </div>
  </section>
</body>
</html>
```